Business card for Autism Consultancy

I need a double-sided business card for Brightpath Learning Consultancy
Please try to use the colours and graphics in line with our website www.brightpathlearn.nz
Front side
Logo and the name of the company – Brightpath Learning Consultancy
We use Child-Centred, Modern and Innovative approaches
Teaching autistic children to bond, laugh and play
www.brightpathlearn.nz
info@brightpathlearn.nz
phone +64 09 37 615 48
Back side
Photo
Mirela Dunstan
Founder
Postgraduate Autism (Children) Specialist (with Merit)
Qualified by the Faculty of Learning Support and Access Studies (FLSA), Harwell Vale University
mirela@brightpathlearn.nz
phone +64 937 615 48
mobile: +64 20 6283 9150
Please do not convert the text fields to outlines, i.e. I need to be able to edit any text after.
The final design should be either in Adobe Illustrator or Adobe Photoshop format.
The Specs for the business card are:
Full Bleed Size
94 x 58 mm
1110 x 685 pixels
Document Trim Size
91 x 55 mm
1075 x 650 pixels

```html
<!DOCTYPE html>
<html lang="en">
<head>
<meta charset="utf-8">
<title>Brightpath Learning Consultancy – Stationery</title>
<link rel="stylesheet" href="https://fonts.googleapis.com/css2?family=Montserrat:ital,wght@0,400;0,500;0,600;0,700;1,400&display=swap">
<style>
  :root {
    --stage: #334550;
    --paper: #ffffff;
    --teal: #53c3be;
    --yellow: #fbd51d;
    --navy: #1e2a5a;
    --ink: #2b2b2b;
    --soft-teal: #d6f1ef;
    --soft-yellow: #fdf3c4;
  }
  * { box-sizing: border-box; margin: 0; padding: 0; }
  html, body { width: 1200px; height: 720px; overflow: hidden; }
  body {
    background: var(--stage);
    font-family: "Montserrat", Arial, sans-serif;
    color: var(--ink);
    position: relative;
  }
  .sheet {
    position: absolute;
    background: var(--paper);
    overflow: hidden;
    box-shadow: 0 10px 18px rgba(0,0,0,.35);
  }
  .card { width: 359px; height: 215px; left: 38px; }
  .card--front { top: 84px; }
  .card--back { top: 345px; }
  .letterhead { left: 460px; top: 79px; width: 333px; height: 475px; }
  .cover { left: 830px; top: 79px; width: 333px; height: 475px; }

  /* decorative areas */
  .deco { position: absolute; }
  .deco--card-top {
    left: 0; top: 0; width: 100%; height: 72px;
    background: linear-gradient(90deg, var(--yellow) 0%, var(--teal) 35%, var(--yellow) 65%, var(--teal) 100%);
    -webkit-mask: linear-gradient(#000 45%, transparent);
            mask: linear-gradient(#000 45%, transparent);
  }
  .deco--card-bottom {
    left: 0; bottom: 0; width: 100%; height: 62px;
    background: linear-gradient(90deg, var(--soft-teal), var(--soft-yellow) 50%, var(--soft-teal));
    -webkit-mask: linear-gradient(transparent, #000 60%);
            mask: linear-gradient(transparent, #000 60%);
  }
  .deco--letter-bottom {
    left: 0; bottom: 0; width: 100%; height: 150px;
    background: linear-gradient(90deg, var(--soft-yellow), var(--soft-teal) 45%, var(--soft-yellow) 80%, var(--soft-teal));
    -webkit-mask: linear-gradient(transparent, #000 45%);
            mask: linear-gradient(transparent, #000 45%);
  }
  .deco--cover {
    left: 0; top: 0; width: 100%; height: 330px;
    background: linear-gradient(135deg, var(--yellow) 0%, var(--teal) 40%, var(--yellow) 70%, var(--teal) 100%);
    -webkit-mask: linear-gradient(#000 70%, transparent);
            mask: linear-gradient(#000 70%, transparent);
  }

  .brand { position: absolute; display: flex; align-items: center; gap: 8px; }
  .brand__dot { border-radius: 50%; background: var(--yellow); flex: none; }
  .brand__name { font-weight: 700; color: var(--navy); line-height: 1.08; letter-spacing: -.2px; }
  .brand--card { left: 92px; top: 88px; }
  .brand--card .brand__dot { width: 30px; height: 30px; }
  .brand--card .brand__name { font-size: 19px; }
  .brand--letter { left: 20px; top: 22px; }
  .brand--letter .brand__dot { width: 18px; height: 18px; }
  .brand--letter .brand__name { font-size: 11.5px; }
  .brand--cover { right: 18px; top: 350px; }
  .brand--cover .brand__dot { width: 22px; height: 22px; }
  .brand--cover .brand__name { font-size: 14px; text-align: right; }
  .watermark {
    position: absolute; left: 0; right: 0; top: 222px; text-align: center;
    font-size: 22px; font-weight: 700; line-height: 1.1; color: #dcdcdc;
  }

  .tagline {
    position: absolute; left: 0; right: 0; top: 162px; text-align: center;
    font-size: 7.3px; font-style: italic; line-height: 1.2;
  }
  .contact-row {
    position: absolute; left: 24px; right: 20px; top: 195px;
    display: flex; justify-content: space-between; font-size: 7.3px;
  }
  .contact { display: flex; align-items: center; gap: 4px; }
  .icon { width: 10px; height: 10px; flex: none; }
  .icon--teal { color: var(--teal); }
  .icon--yellow { color: var(--yellow); }

  .portrait {
    position: absolute; left: 31px; top: 64px; width: 102px; height: 102px;
    border-radius: 50%; background: var(--yellow);
    display: flex; align-items: center; justify-content: center;
  }
  .portrait__photo {
    width: 90px; height: 90px; border-radius: 50%;
    border: 2px solid var(--teal);
    background: radial-gradient(circle at 50% 40%, #c99a80 0%, #6d4a37 55%, #3a2a22 100%);
  }
  .divider {
    position: absolute; left: 156px; top: 60px; width: 1px; height: 115px;
    background: linear-gradient(#e4e4e4, rgba(228,228,228,0));
  }
  .profile { position: absolute; left: 170px; top: 68px; width: 180px; }
  .profile__name { font-size: 15.5px; font-weight: 600; color: var(--teal); line-height: 1; }
  .profile__role { font-size: 6px; font-style: italic; margin-top: 3px; }
  .profile__bio { font-size: 5.6px; font-style: italic; line-height: 1.3; margin-top: 6px; }
  .profile__list { list-style: none; margin-top: 8px; font-size: 7.2px; line-height: 1.25; }
  .profile__list li { display: flex; gap: 6px; margin-bottom: 6px; }

  .stack { position: absolute; list-style: none; font-size: 7.4px; line-height: 1.25; }
  .stack li { display: flex; gap: 6px; margin-bottom: 4px; }
  .stack--letter { left: 16px; top: 411px; }
  .stack--cover { left: 205px; top: 412px; }
</style>
</head>
<body>

<svg width="0" height="0" style="position:absolute" aria-hidden="true">
  <symbol id="i-globe" viewBox="0 0 20 20"><circle cx="10" cy="10" r="8.5" fill="none" stroke="currentColor" stroke-width="1.6"/><ellipse cx="10" cy="10" rx="3.8" ry="8.5" fill="none" stroke="currentColor" stroke-width="1.4"/><path d="M1.5 10h17M3 5.5h14M3 14.5h14" stroke="currentColor" stroke-width="1.3"/></symbol>
  <symbol id="i-mail" viewBox="0 0 20 20"><rect x="1.5" y="4" width="17" height="12" fill="currentColor"/><path d="M1.5 4l8.5 7 8.5-7M1.5 16l6-6M18.5 16l-6-6" fill="none" stroke="#fff" stroke-width="1.3"/></symbol>
  <symbol id="i-phone" viewBox="0 0 20 20"><path d="M5 1.5l3 4-2 2.2c1 2.6 3.3 4.9 5.8 5.8l2.2-2 4 3-1.8 3.5C9 17.5 2.5 11 2 3.3z" fill="currentColor"/></symbol>
</svg>

<section class="sheet card card--front" aria-label="Business card front">
  <div class="deco deco--card-top" role="img" aria-label="Decorative yellow and teal bubble pattern"></div>
  <div class="brand brand--card">
    <span class="brand__dot"></span>
    <p class="brand__name">Brightpath Learning<br>Consultancy</p>
  </div>
  <p class="tagline">We use Child-Centred, Modern and Innovative approaches<br>Teaching autistic children to bond, laugh and play</p>
  <div class="contact-row">
    <span class="contact"><svg class="icon icon--yellow"><use href="#i-globe"/></svg>www.brightpathlearn.nz</span>
    <span class="contact"><svg class="icon icon--yellow"><use href="#i-mail"/></svg>info@brightpathlearn.nz</span>
    <span class="contact"><svg class="icon icon--yellow"><use href="#i-phone"/></svg>+64 09 37 615 48</span>
  </div>
</section>

<section class="sheet card card--back" aria-label="Business card back">
  <div class="deco deco--card-top" role="img" aria-label="Decorative yellow and teal bubble pattern"></div>
  <div class="deco deco--card-bottom" role="img" aria-label="Decorative pale bubble pattern"></div>
  <div class="portrait"><div class="portrait__photo" role="img" aria-label="Portrait photo of Mirela Dunstan, founder"></div></div>
  <div class="divider"></div>
  <div class="profile">
    <h1 class="profile__name">Mirela Dunstan</h1>
    <p class="profile__role">CEO/FOUNDER</p>
    <p class="profile__bio">Postgraduate Autism (Children) Specialist (with Merit)<br>Qualified by the Faculty of Learning Support and Access Studies (FLSA), Harwell Vale University</p>
    <ul class="profile__list">
      <li><svg class="icon icon--yellow"><use href="#i-mail"/></svg>mirela@brightpathlearn.nz</li>
      <li><svg class="icon icon--yellow"><use href="#i-phone"/></svg><span>Mobile: +64 20 6283 9150<br>Phone +64 937 615 48</span></li>
    </ul>
  </div>
</section>

<section class="sheet letterhead" aria-label="Letterhead">
  <div class="deco deco--letter-bottom" role="img" aria-label="Decorative pale bubble pattern"></div>
  <div class="brand brand--letter">
    <span class="brand__dot"></span>
    <p class="brand__name">Brightpath Learning<br>Consultancy</p>
  </div>
  <p class="watermark">Brightpath Learning<br>Consultancy</p>
  <ul class="stack stack--letter">
    <li><svg class="icon icon--teal"><use href="#i-mail"/></svg>info@brightpathlearn.nz</li>
    <li><svg class="icon icon--teal"><use href="#i-globe"/></svg>www.brightpathlearn.nz</li>
    <li><svg class="icon icon--teal"><use href="#i-phone"/></svg><span>Mobile: +64 20 6283 9150<br>Phone +64 937 615 48</span></li>
  </ul>
</section>

<section class="sheet cover" aria-label="Folder cover">
  <div class="deco deco--cover" role="img" aria-label="Decorative large yellow and teal bubble pattern"></div>
  <div class="brand brand--cover">
    <span class="brand__dot"></span>
    <p class="brand__name">Brightpath Learning<br>Consultancy</p>
  </div>
  <ul class="stack stack--cover">
    <li><svg class="icon icon--teal"><use href="#i-mail"/></svg>info@brightpathlearn.nz</li>
    <li><svg class="icon icon--teal"><use href="#i-globe"/></svg>www.brightpathlearn.nz</li>
    <li><svg class="icon icon--teal"><use href="#i-phone"/></svg><span>Mobile: +64 20 6283 9150<br>Phone +64 937 615 48</span></li>
  </ul>
</section>

</body>
</html>
```